Zielgruppe
Wir sind ein Vertriebsunternehmen, mit dem Ziel die klassische Finanz und den Kryptosektor zu verbinden. Unsere Zielgruppe sind Menschen zwischn 25 - 45 Jahre. Wir sind die Communty und Vertrieb der ersten rechtkonformen STO - Plattform ( Plattform für Wertpapiere im Kryptosektor)
Diese Projekt ist Teil eines Paketes, wir bitten nur Designer mit zu machen die alle benötigten Unterlagen designen können. (siehe restliche Projekte) - Gesamtvolumen: 2300€ Preisgeld
Online-Marketing Material
2 Vorlagen Social Media - (Einladung/Event, Sprüche/Information)
Banner
Präsentationsvorlagen - min unterschiedliche 8 Vorlagenseiten /Layouts.
Landingpage Layout f. Funnelsite für Webinaranmeldung mit Platz für Formular
Newsletter Layoutvorlage
Vorlage Infografik
Broschüre / E - Book Designe
Es werden nur Vorlagen benötigt mit 'LoremSum Texten' und Musterbildern. Wir möchten von allen Vorlagen die Originaldatei, uns stehen folgende Grafikprogramme zur Verfügung:
Adobe Photoshop
Adobe Illustrator
Canva
Newsletter und Landingpage Software: postflinkel.com
Unsere Akt. Designe (Designe Alt) gefällt uns von der Idee, dennoch wünschen wir es uns moderner und edler mit ein wenig 'spaceig'. - Eben die Vereinigung von Kryptowelt und klassischer Finanz.
Schriftart: Poppins
Farben lt. Logo
Aufgabenstellung
Diese Projekt ist Teil eines Paketes, wir bitten nur Designer mit zu machen die alle benötigten Unterlagen designen können. (siehe restliche Projekte) - Gesamtvolumen: 2000€ - 2300€ Preisgeld

```html
<!DOCTYPE html>
<html lang="de">
<head>
<meta charset="utf-8">
<title>Webinar – Veranstaltung</title>
<link rel="stylesheet" href="https://fonts.googleapis.com/css2?family=Poppins:wght@400;500;600;700&display=swap">
<style>
  :root {
    --page-bg: #e4e6f1;
    --card-top: #2159a8;
    --card-bottom: #184a92;
    --white: #ffffff;
    --panel: rgba(205, 218, 238, 0.88);
    --panel-edge: rgba(160, 185, 220, 0.8);
    --ink: #28323f;
    --button: #2d4f9c;
    --button-edge: #3d62b4;
  }
  * { margin: 0; padding: 0; box-sizing: border-box; }
  html, body {
    width: 1200px; height: 1199px; overflow: hidden;
    background: var(--page-bg);
    font-family: "Poppins", sans-serif;
  }
  .card {
    position: absolute; left: 44px; top: 44px; width: 1113px; height: 1112px;
    border-radius: 26px; overflow: hidden;
    background: radial-gradient(ellipse at 70% 55%, #2a66b8 0%, transparent 60%),
                linear-gradient(180deg, var(--card-top), var(--card-bottom));
  }
  .brand {
    position: absolute; left: 30px; top: 150px;
    display: flex; align-items: center; gap: 14px;
    color: var(--white); font-weight: 600; font-size: 36px;
  }
  .brand-dot { width: 34px; height: 34px; border-radius: 50%; background: var(--white); }
  .headline { position: absolute; left: 392px; top: 58px; color: var(--white); }
  .headline .kicker { font-size: 48px; font-weight: 500; line-height: 62px; letter-spacing: 0.2px; }
  .headline .title { font-size: 80px; font-weight: 700; line-height: 92px; letter-spacing: 0.5px; }
  .intro {
    position: absolute; left: 111px; top: 386px; width: 700px;
    color: var(--white); font-size: 32px; line-height: 48.5px;
  }
  .benefits {
    position: absolute; left: 111px; top: 542px; list-style: none;
    color: var(--white); font-size: 29px; line-height: 51px;
  }
  .benefits li { display: flex; align-items: center; gap: 6px; }
  .benefits svg { width: 28px; height: 28px; }
  .panel { position: absolute; left: 0; top: 0; }
  .photo-circle { position: absolute; left: 643px; top: 692px; width: 560px; height: 560px; border-radius: 50%;
    background: radial-gradient(circle at 55% 45%, #9fb6d9 0%, #6f93c8 55%, #4d78b8 100%); opacity: 0.9; }
  .photo {
    position: absolute; left: 700px; top: 690px; width: 440px; height: 422px;
    border-radius: 180px 180px 0 0;
    background: linear-gradient(160deg, #e9edf2 0%, #c9d3df 45%, #9fb3cb 100%);
  }
  .event { position: absolute; left: 113px; top: 718px; color: var(--ink); }
  .event .date { font-size: 42px; font-weight: 700; line-height: 52px; letter-spacing: 0.3px; }
  .event .time { font-size: 42px; font-weight: 500; line-height: 52px; }
  .signup {
    position: absolute; left: 113px; top: 838px; width: 393px; height: 88px;
    background: var(--button); border: 6px solid var(--button-edge); border-radius: 8px;
    color: var(--white); font-size: 37px; display: flex; align-items: center; justify-content: center;
  }
  .contacts { position: absolute; left: 113px; top: 941px; list-style: none; color: var(--ink); font-size: 20.5px; line-height: 38px; }
  .contacts li { display: flex; align-items: center; gap: 8px; }
  .contacts svg { width: 24px; height: 24px; }
</style>
</head>
<body>
<main class="card">
  <div class="brand"><span class="brand-dot"></span>GreenKestrel</div>

  <header class="headline">
    <p class="kicker">Muster Text Lorem Ipsum</p>
    <h1 class="title">Webinar –<br>Veranstaltung</h1>
  </header>

  <p class="intro">Muster kurze Beschreibung Lorem ipsum dolor sit est consetetur sadipscing elitr sed diam nonumy eirmod tempor.</p>

  <ul class="benefits">
    <li><svg viewBox="0 0 24 24" fill="none" stroke="#fff" stroke-width="2"><path d="M3 13l5 5L21 5M3 9l5 5"/></svg>Lorem ipsum dolor sit amet consetetur.</li>
    <li><svg viewBox="0 0 24 24" fill="none" stroke="#fff" stroke-width="2"><path d="M3 13l5 5L21 5M3 9l5 5"/></svg>Sadipscing elitr, sed diam ils eirmod.</li>
  </ul>

  <svg class="panel" width="1113" height="1112" viewBox="0 0 1113 1112">
    <path d="M100 694 H710 C640 760 600 880 598 1078 H100 Q60 1078 60 1038 V734 Q60 694 100 694 Z" fill="var(--panel)" stroke="var(--panel-edge)" stroke-width="1.5"/>
  </svg>

  <div class="photo-circle"></div>
  <div class="photo" role="img" aria-label="Foto: junger Mann mit Laptop sitzt lächelnd auf einem weißen Stuhl"></div>

  <div class="event">
    <p class="date">DO. 27.7.2023</p>
    <p class="time">20:30 Uhr</p>
  </div>
  <div class="signup">Anmeldelink</div>

  <ul class="contacts">
    <li><svg viewBox="0 0 24 24" fill="none" stroke="#28323f" stroke-width="1.6"><path d="M5 3h4l2 5-3 2a12 12 0 0 0 6 6l2-3 5 2v4a2 2 0 0 1-2 2A18 18 0 0 1 3 5a2 2 0 0 1 2-2z"/></svg>(01) 0987 654 321</li>
    <li><svg viewBox="0 0 24 24" fill="none" stroke="#28323f" stroke-width="1.8"><circle cx="12" cy="12" r="4"/><path d="M16 12v1.5a2.5 2.5 0 0 0 5 0V12a9 9 0 1 0-3.5 7.1"/></svg>info@greenkestrel.investments</li>
    <li><svg viewBox="0 0 24 24" fill="none" stroke="#28323f" stroke-width="1.6"><circle cx="12" cy="12" r="9"/><path d="M3 12h18M12 3c3 3 3 15 0 18M12 3c-3 3-3 15 0 18M5 7h14M5 17h14"/></svg>www.greenkestrel.investments</li>
  </ul>
</main>
</body>
</html>
```